New writer needs an ebook cover design

My book is a non-fiction travelogue where I travel around every brewery in Scotland in an old Dutch campervan called Gerald. The book is called 'The Copper Kettle Riddle' with the subtitle 'Chasing hops across the misty glens'. The image will need to work as a thumbprint as well as full-size. The key aspects of the book would be beer (craft beer, real ale etc, not corporate brands), Gerald and Scotland. The reader should feel that they are riding along with Gerald, discovering beer and Scotland as I make my way to remote locations and islands, visiting sixty breweries as we go. The book is not a technical guide or for reference purposes. Design must be suitable for Pellora Reader upload. Cheers!

Target Market(s)

Lovers of beer, travel, Scotland and campervans

Industry/Entity Type

Brewery

Requirements
Must have
• The title, subtitle and author's name - Douglas Farquhar. Also things that, directly or indirectly, convey some or all of beer, campervan and Scotland.
Nice to have
• A beermat or pumpclip with Gerald on it would be one suggestion for the central part of the image. An actual image of Gerald, be it real or cartooned could be used plus something to suggest Scotland.
Should not have
• Puns

```html
<!DOCTYPE html>
<html lang="en">
<head>
<meta charset="utf-8">
<title>The Copper Kettle Riddle — Douglas Farquhar</title>
<link rel="stylesheet" href="https://fonts.googleapis.com/css2?family=Coustard:wght@400;900&family=Montserrat:wght@600&display=swap">
<style>
  :root {
    --wood-dark: #2a1a10;
    --wood-mid: #4a2f1e;
    --wood-light: #5d3c27;
    --label-cream: #e6ddbd;
    --label-tan: #b7a67a;
    --label-shadow: #1b110a;
    --stripe-red: #8d2b2b;
    --ink-green: #4b5a38;
    --van-grey: #cfc6ad;
    --van-shade: #9d9581;
    --author-white: #f4f1ea;
  }
  html, body {
    margin: 0;
    padding: 0;
    overflow: hidden;
    background: var(--wood-dark);
  }
  .cover {
    position: relative;
    width: 751px;
    height: 1200px;
    overflow: hidden;
  }
  .wood-backdrop {
    position: absolute;
    inset: 0;
    background:
      linear-gradient(180deg, var(--wood-mid) 0%, var(--wood-light) 30%, var(--wood-mid) 55%, var(--wood-light) 80%, var(--wood-dark) 100%);
  }
  .label-art {
    position: absolute;
    inset: 0;
  }
  .title-text,
  .subtitle-text {
    font-family: "Coustard", Georgia, serif;
    font-weight: 900;
    fill: var(--ink-green);
  }
  .van-name {
    font-family: "Coustard", Georgia, serif;
    font-weight: 900;
    fill: #6b6453;
    letter-spacing: 2px;
  }
  .author {
    position: absolute;
    left: 0;
    right: 0;
    top: 1092px;
    margin: 0;
    text-align: center;
    font-family: "Montserrat", Arial, sans-serif;
    font-weight: 600;
    font-size: 38px;
    letter-spacing: 5px;
    color: var(--author-white);
  }
</style>
</head>
<body>
<main class="cover">
  <div class="wood-backdrop" role="img" aria-label="Dark weathered wooden planks running horizontally"></div>

  <svg class="label-art" width="751" height="1200" viewBox="0 0 751 1200">
    <defs>
      <path id="title-arch" d="M140,470 C140,290 250,178 376,178 C502,178 612,290 612,470"/>
    </defs>

    <g class="pump-clip">
      <path class="clip-shadow" fill="var(--label-shadow)" opacity="0.55"
            d="M75,452 C75,250 215,112 380,112 C545,112 689,250 689,452 L689,628 C689,810 545,950 380,950 C215,950 75,810 75,628 Z"/>
      <path class="clip-rim" fill="var(--label-tan)"
            d="M69,440 C69,240 210,104 376,104 C542,104 683,240 683,440 L683,620 C683,800 542,940 376,940 C210,940 69,800 69,620 Z"/>
      <path class="clip-face" fill="var(--label-cream)"
            d="M78,440 C78,246 216,113 376,113 C536,113 674,246 674,440 L674,620 C674,794 536,931 376,931 C216,931 78,794 78,620 Z"/>
      <path class="clip-stripe-outer" fill="none" stroke="var(--stripe-red)" stroke-width="7"
            d="M92,440 C92,256 224,128 376,128 C528,128 660,256 660,440 L660,620 C660,786 528,917 376,917 C224,917 92,786 92,620 Z"/>
      <path class="clip-stripe-inner" fill="none" stroke="var(--stripe-red)" stroke-width="4"
            d="M108,440 C108,266 232,143 376,143 C520,143 644,266 644,440 L644,620 C644,776 520,902 376,902 C232,902 108,776 108,620 Z"/>

      <path class="van-arch" fill="none" stroke="var(--label-tan)" stroke-width="5"
            d="M240,520 L240,380 C240,318 300,278 376,278 C452,278 512,318 512,380 L512,520"/>

      <text class="title-text" font-size="48">
        <textPath href="#title-arch" startOffset="50%" text-anchor="middle">The Copper Kettle</textPath>
      </text>

      <g class="campervan">
        <rect x="252" y="318" width="248" height="150" rx="14" fill="var(--van-grey)"
              role="img" aria-label="Illustration of Gerald, an old boxy campervan with a raised roof, seen from the side"/>
        <rect x="252" y="430" width="248" height="38" rx="10" fill="var(--van-shade)" opacity="0.45"/>
        <text class="van-name" x="362" y="345" font-size="18" text-anchor="middle">GERALD</text>
      </g>

      <rect class="banner-rim" x="37" y="514" width="679" height="144" rx="10" fill="var(--label-tan)"/>
      <rect class="banner-stripe" x="45" y="522" width="663" height="128" rx="8" fill="var(--stripe-red)"/>
      <rect class="banner-face" x="54" y="531" width="645" height="110" rx="6" fill="var(--label-cream)"/>
      <text class="title-text" x="376" y="622" font-size="100" text-anchor="middle" letter-spacing="2">RIDDLE</text>

      <g class="subtitle">
        <text class="subtitle-text" x="338" y="716" font-size="30" text-anchor="end">Chasing</text>
        <text class="subtitle-text" x="346" y="744" font-size="64">Hops</text>
        <text class="subtitle-text" x="232" y="770" font-size="22">across</text>
        <text class="subtitle-text" x="322" y="790" font-size="22">the misty</text>
        <text class="subtitle-text" x="236" y="852" font-size="72">Glens</text>
      </g>
    </g>
  </svg>

  <p class="author">DOUGLAS FARQUHAR</p>
</main>
</body>
</html>
```